Quillmere Business Advisory Business Card Design Project

I have a new business called Quillmere Business Advisory Limited. We provide business services for the UK for areas which include

Mentoring / Coaching
Interim Management
Non Executive Director / Chairman placement
Angel Investment support
Merger & Acquisition advice
Selling your business advice

I would like a background colour on the logo, a logo and our company name on the logo if possible.

I am open to colours but we want to portray a strong safe business with credibility

The business card design must match that of the logo design

Target Market(s)

SME and Medium size businesses with the owners, MD's, CEO or senior management as the target audiabce

Industry/Entity Type

Business

Requirements
Must have
• Match the logo design.
Look professional and quality
Should not have
• Old style text and colours
Poor logos depicting money

```html
<!DOCTYPE html>
<html lang="en">
<head>
<meta charset="utf-8">
<title>Quillmere Business Advisory – Business Card</title>
<link rel="stylesheet" href="https://fonts.googleapis.com/css2?family=Open+Sans:wght@400&display=swap">
<style>
  :root {
    --backdrop: #e4dfd8;
    --card-top: #f3f1ee;
    --card-bottom: #e9e6e2;
    --accent-block: #3f3a6e;
    --logo-navy: #2a2f6b;
    --ink: #333333;
    --name-blue: #3a6a9c;
  }
  * { margin: 0; padding: 0; box-sizing: border-box; }
  html, body {
    width: 1200px;
    height: 970px;
    overflow: hidden;
    background: var(--backdrop);
    font-family: "Open Sans", Arial, sans-serif;
  }
  .business-card {
    position: absolute;
    left: 100px;
    top: 207px;
    width: 1000px;
    height: 556px;
    background: linear-gradient(180deg, var(--card-top), var(--card-bottom));
    box-shadow: 0 8px 30px rgba(0,0,0,0.15);
    color: var(--ink);
  }
  .accent-block {
    position: absolute;
    left: 0;
    top: 160px;
    width: 241px;
    height: 248px;
    background: var(--accent-block);
    border-radius: 0 8px 8px 0;
  }
  .brand-mark {
    position: absolute;
    right: 43px;
    top: 40px;
    display: flex;
    align-items: center;
    gap: 14px;
  }
  .brand-mark__name {
    font-size: 30px;
    color: var(--logo-navy);
    letter-spacing: 0.5px;
  }
  .brand-mark svg { display: block; }
  .company-name {
    position: absolute;
    right: 13px;
    top: 180px;
    font-size: 25px;
    letter-spacing: 0.6px;
  }
  .person {
    position: absolute;
    right: 43px;
    top: 268px;
    text-align: right;
  }
  .person__name {
    font-size: 29px;
    color: var(--name-blue);
    line-height: 1.1;
    letter-spacing: 0.4px;
  }
  .person__role {
    font-size: 22px;
    line-height: 1.1;
  }
  .contact {
    position: absolute;
    right: 43px;
    top: 416px;
    text-align: right;
    font-size: 22px;
    line-height: 24.5px;
    letter-spacing: 0.5px;
  }
</style>
</head>
<body>
  <main class="business-card">
    <div class="accent-block"></div>

    <div class="brand-mark">
      <span class="brand-mark__name">Quillmere</span>
      <svg width="60" height="60" viewBox="0 0 60 60" aria-hidden="true">
        <circle cx="30" cy="30" r="27" fill="none" stroke="#555" stroke-width="2"/>
      </svg>
    </div>

    <h1 class="company-name" style="font-weight:400">Quillmere Business Advisory Limited</h1>

    <div class="person">
      <p class="person__name">Sample Name</p>
      <p class="person__role">CEO</p>
    </div>

    <address class="contact" style="font-style:normal">
      Tel: 192-555-0148<br>
      Cell: 310-555-0172<br>
      Email: yourname@quillmere.com<br>
      2210 Harbour Row, Suite 1040<br>
      Riverside, CA 92501
    </address>
  </main>
</body>
</html>
```